I need a business card design for a new company that will be doing consulting work around issues of cultural competency, and diversity and inclusion. I would like the design to be crisp and clear with bold but conservative colors and incorporate shades of blue

Target Market(s)

Small businesses, schools, non-profits

Industry/Entity Type

Consulting

Font styles to use
Serif
Sans Serif

Colors
0c5ba6
6b449b
3276b5
0292cd

Requirements
Must have
• A Morrow Venture (name of company)
• Lemlem Tavish
• CEO
• lemlem@amorrowventure.com
• (215)483-2756

```html
<!DOCTYPE html>
<html lang="en">
<head>
<meta charset="utf-8">
<title>A Morrow Venture — Business Card</title>
<link rel="stylesheet" href="https://fonts.googleapis.com/css2?family=Montserrat:wght@300;400;500;700;800&display=swap">
<style>
  :root {
    --paper: #ffffff;
    --sky: #0292cd;
    --violet: #6b449b;
    --navy-fold: #1c3d6e;
    --guide: #1a1a1a;
    --ink-light: #ffffff;
  }
  * { margin: 0; padding: 0; box-sizing: border-box; }
  html, body {
    width: 1200px; height: 720px; overflow: hidden;
    background: var(--paper);
  }
  .card {
    position: relative; width: 1200px; height: 720px;
    background: var(--paper);
    font-family: "Montserrat", Arial, sans-serif;
  }
  .card-art { position: absolute; inset: 0; }
  .brand {
    position: absolute; left: 0; top: 216px; width: 560px;
    text-align: center;
  }
  .brand-mark {
    width: 158px; height: 158px; margin: 0 auto 0 186px;
    border-radius: 50%; background: var(--violet);
    display: flex; align-items: center; justify-content: center;
    color: var(--ink-light); font-weight: 400; font-size: 24px;
    line-height: 1.3; letter-spacing: 0.5px; text-align: center;
  }
  .brand-name {
    position: absolute; left: 0; top: 168px; width: 596px;
    text-align: center; white-space: nowrap;
    color: var(--violet); font-weight: 700; font-size: 40px;
  }
  .tab {
    position: absolute; left: 558px;
    background: var(--violet); color: var(--ink-light);
    white-space: nowrap;
  }
  .tab-name {
    top: 100px; height: 124px;
    padding: 10px 38px 0 22px;
    border-radius: 0 26px 26px 0;
  }
  .person-name { font-weight: 800; font-size: 52px; line-height: 1.1; letter-spacing: 0.5px; }
  .person-role { font-weight: 300; font-size: 34px; letter-spacing: 7px; line-height: 1.1; }
  .tab-contact {
    height: 62px; padding: 0 16px 0 19px;
    border-radius: 0 7px 7px 0;
    display: flex; align-items: center;
    font-weight: 400; font-size: 35px;
  }
  .tab-email { top: 382px; }
  .tab-phone { top: 473px; }
</style>
</head>
<body>
<main class="card">
  <svg class="card-art" width="1200" height="720" viewBox="0 0 1200 720" aria-hidden="true">
    <rect class="contact-panel" x="569" y="38" width="631" height="639" fill="var(--sky)"/>
    <g class="trim-guides" stroke="var(--guide)" stroke-width="2.5" stroke-dasharray="5 4" fill="none">
      <line x1="0" y1="73" x2="1200" y2="73"/>
      <line x1="0" y1="642" x2="1200" y2="642"/>
      <line x1="36" y1="42" x2="36" y2="675"/>
      <line x1="1159" y1="42" x2="1159" y2="675"/>
    </g>
    <g class="tab-folds" fill="var(--navy-fold)">
      <path d="M558,222 L572,222 C568,232 566,244 570,256 C564,246 559,236 558,222 Z"/>
      <path d="M558,442 L572,442 C568,452 566,464 570,476 C564,466 559,456 558,442 Z"/>
      <path d="M558,533 L572,533 C568,543 566,555 570,567 C564,557 559,547 558,533 Z"/>
    </g>
  </svg>

  <section class="brand">
    <div class="brand-mark">YOUR<br>LOGO</div>
    <p class="brand-name">A Morrow Venture</p>
  </section>

  <header class="tab tab-name">
    <h1 class="person-name">Lemlem Tavish</h1>
    <p class="person-role">CEO</p>
  </header>
  <p class="tab tab-contact tab-email">lemlem@amorrowventure.com</p>
  <p class="tab tab-contact tab-phone">(215)483-2756</p>
</main>
</body>
</html>
```